Van/Car Signage

I'm looking for artwork designs for signwriting for our company cars & Vans. 1 x 2023 Vorlan Tessaro Ridge & 1 x 2024 Mirex Haulmate LWB Both are White. You can access our company details and product range at www.quellmorefittingsco.com.au - i have uploaded our logo.

```html
<!DOCTYPE html>
<html lang="en">
<head>
<meta charset="utf-8">
<title>Quellmore Fittings Co – Vehicle Signage</title>
<link rel="stylesheet" href="https://fonts.googleapis.com/css2?family=Poppins:wght@600;700&family=Archivo:ital,wght@1,800&display=swap">
<style>
  :root {
    --bg: #eceeee;
    --red-light: #e21b24;
    --red-dark: #b3101d;
    --blue: #1f74c4;
    --white: #ffffff;
  }
  html, body {
    margin: 0;
    padding: 0;
    width: 900px;
    height: 1200px;
    overflow: hidden;
    background: var(--bg);
  }
  .signage-sheet {
    display: block;
    width: 900px;
    height: 1200px;
  }
  .brand-name {
    font-family: "Poppins", sans-serif;
    font-weight: 700;
    fill: var(--white);
  }
  .brand-sub {
    font-family: "Poppins", sans-serif;
    font-weight: 600;
    fill: var(--white);
    letter-spacing: 3px;
  }
  .contact-line {
    font-family: "Archivo", sans-serif;
    font-style: italic;
    font-weight: 800;
    fill: var(--white);
  }
  .accent-stripe { fill: var(--blue); }
  .livery-panel { fill: url(#livery-red); }
  .rule { stroke: var(--white); stroke-width: 3; }
</style>
</head>
<body>
<svg class="signage-sheet" viewBox="0 0 1659 2212" xmlns="http://www.w3.org/2000/svg" role="img" aria-label="Side livery artwork for an SUV and a long-wheelbase van">
  <defs>
    <linearGradient id="livery-red" x1="0" y1="0" x2="1" y2="0">
      <stop offset="0" stop-color="var(--red-light)"/>
      <stop offset="1" stop-color="var(--red-dark)"/>
    </linearGradient>
  </defs>

  <!-- SUV side livery -->
  <g class="livery livery--suv">
    <polygon class="accent-stripe" points="395,553 635,497 1163,566 1162,580 635,512 400,565"/>
    <path class="livery-panel" d="M425,568 L635,518 L1160,584 L1150,708 L500,710 C492,640 468,595 425,568 Z"/>
    <g class="brand-lockup">
      <text class="brand-name" x="641" y="650" font-size="36" text-anchor="middle">Quellmore</text>
      <line class="rule" x1="540" y1="662" x2="572" y2="662"/>
      <text class="brand-sub" x="641" y="667" font-size="14" text-anchor="middle">FITTINGS CO</text>
      <line class="rule" x1="710" y1="662" x2="742" y2="662"/>
    </g>
    <g class="contact-block">
      <text class="contact-line" x="887" y="630" font-size="13">Free Measure &amp; Quote</text>
      <text class="contact-line" x="887" y="648" font-size="13" letter-spacing="3">(03) 9471 5820</text>
      <text class="contact-line" x="887" y="664" font-size="8">sales@quellmorefittingsco.com.au</text>
    </g>
  </g>

  <!-- Van side livery -->
  <g class="livery livery--van">
    <polygon class="accent-stripe" points="118,1780 500,1688 1610,1833 1610,1848 500,1703 118,1795"/>
    <path class="livery-panel" d="M118,1803 L500,1712 L1610,1857 L1622,1885 L1600,1935 L1480,1935 C1470,1870 1420,1835 1365,1835 C1300,1835 1255,1880 1250,1935 L475,1925 C470,1860 420,1810 350,1810 C280,1810 235,1855 230,1880 L135,1880 Z"/>
    <g class="brand-lockup">
      <text class="brand-name" x="673" y="1896" font-size="40" text-anchor="middle">Quellmore</text>
      <line class="rule" x1="550" y1="1909" x2="586" y2="1909"/>
      <text class="brand-sub" x="673" y="1915" font-size="15" text-anchor="middle">FITTINGS CO</text>
      <line class="rule" x1="760" y1="1909" x2="796" y2="1909"/>
    </g>
    <g class="contact-block">
      <text class="contact-line" x="1023" y="1850" font-size="13">Free Measure &amp; Quote</text>
      <text class="contact-line" x="1023" y="1869" font-size="13" letter-spacing="3">(03) 9471 5820</text>
      <text class="contact-line" x="1023" y="1884" font-size="8">sales@quellmorefittingsco.com.au</text>
    </g>
  </g>
</svg>
</body>
</html>
```